Brack and Loam LLC | Land Clearing, Landscaping & Dump Trailer Services

Project Description: Brack and Loam LLC Website Design
The website will be published using squarespace
Objective:
Design a visually compelling and conversion-driven website for Brack and Loam LLC, a land solutions business based in Pickens County, Georgia. The site will highlight the company’s professionalism, locally rooted service, and commitment to quality in land clearing, grading, and dump trailer services.
Pages & Features to Include:
1. Landing Page (Homepage)
- Clear tagline: Shaping Ground with Care and Grit
- Call-to-Action (CTA) buttons: “Get a Free Quote” and “View Services”
- Service highlights with icons or photos (e.g., grading, mulching, hauling)
- Customer testimonials
- Embedded contact form
- Google Maps integration showing service area
2. Services + Pricing Page
- Organized list of services under 3 categories:
- **Land Clearing & Grading**
- Forestry Mulching
- Gravel Driveway Repair
- Minimum Job Fee:
- Dump Trailer Services
- Trailer Rental (Daily):
- Junk Removal (Full Load)
- Material Delivery: $ + mileage
- Specialty Jobs
- Stump removal, light demolition
- Each service section includes short descriptions and photos
- Optional quote form at the bottom with “Request a Quote” CTA
Design Style:
- Clean, professional design using clean tones
- Fonts that balance industrial strength and local charm
- Mobile-optimized with fast loading speeds and easy navigation
- SEO-optimized for terms like *land clearing Pickens County*, *grading services North Georgia*, and *dump trailer rental Jasper GA*, etc...

```html
<!DOCTYPE html>
<html lang="en">
<head>
<meta charset="utf-8">
<title>Brack and Loam LLC | Land Clearing, Grading &amp; Dump Trailer Services</title>
<link rel="stylesheet" href="https://fonts.googleapis.com/css2?family=Red+Hat+Display:wght@400;500;600;700&display=swap">
<style>
:root{
  --green:#4a9a2c;
  --green-dark:#3f8624;
  --dark:#333333;
  --darker:#2a2a2a;
  --mint:#ebf2e7;
  --grey-box:#ececec;
  --text:#2b2b2b;
  --muted:#555;
  --white:#fff;
  --line:#bfbfbf;
}
*{box-sizing:border-box;margin:0;padding:0}
html,body{width:1200px;height:4213px;overflow:hidden}
body{font-family:"Red Hat Display",Arial,sans-serif;color:var(--text);background:var(--white)}
.page{position:relative;width:1200px;height:4213px;overflow:hidden}
.abs{position:absolute}
.btn{position:absolute;display:flex;align-items:center;justify-content:center;border-radius:40px;font-size:11px;font-weight:600;text-decoration:none;white-space:nowrap}
.btn-green{background:var(--green);color:var(--white)}
.btn-white{background:var(--white);color:var(--text)}
.btn-outline{border:1.5px solid var(--green);color:var(--text);background:transparent}
.btn-outline-light{border:1.5px solid var(--green);color:var(--white)}
.btn-dark{background:var(--dark);color:var(--white)}
.section-title{position:absolute;left:200px;font-size:39px;font-weight:500;letter-spacing:-.2px}
.rule{position:absolute;left:0;height:1px;background:var(--line)}
.lead{position:absolute;left:381px;font-size:11.5px;line-height:15px}

/* header */
.site-header{position:absolute;left:0;top:0;width:1200px;height:74px;background:var(--dark);z-index:3}
.brand-badge{position:absolute;left:77px;top:22px;width:86px;height:84px;background:var(--darker);border-radius:4px;display:flex;align-items:center;justify-content:center;gap:5px;z-index:4}
.brand-badge .mark{width:9px;height:9px;background:var(--green)}
.brand-badge span{color:var(--white);font-size:12px;font-weight:700;line-height:13px}
.nav{position:absolute;left:381px;top:30px;display:flex;font-size:10.5px;color:var(--white)}
.nav a{color:var(--white);text-decoration:none;margin-right:32px}
.nav a.current{color:var(--green)}
.header-phone{position:absolute;left:855px;top:29px;color:var(--white);font-size:11px;display:flex;align-items:center;gap:5px}

/* hero */
.hero{position:absolute;left:0;top:0;width:1200px;height:625px;background:linear-gradient(180deg,#7d8f97 0%,#5c7463 22%,#3f5c33 45%,#4f6236 62%,#7e7256 78%,#8d7b60 100%)}
.hero h1{position:absolute;left:200px;top:228px;color:var(--white);font-size:51px;font-weight:500;line-height:57px}
.dots{position:absolute;left:199px;top:550px;display:flex;gap:12px}
.dots i{width:13px;height:13px;border-radius:50%;background:var(--white);display:block}
.dots i.on{background:transparent;border:2.5px solid #5fb83a}

/* about */
.about-frame{position:absolute;left:75px;top:625px;width:250px;height:511px;border-left:25px solid var(--green);border-top:19px solid var(--green)}
.about-frame::after{content:"";position:absolute;left:0;top:0;width:240px;height:520px;background:var(--white)}
.about h2{top:728px}
.about .sub{position:absolute;left:200px;top:846px;font-size:14px;font-weight:600;line-height:15px;width:380px}
.about p.body{position:absolute;left:200px;width:510px;font-size:9.6px;line-height:16px;color:var(--muted)}
.photo-circle{position:absolute;border-radius:50%}

/* services */
.services-band{position:absolute;left:0;top:1542px;width:1200px;height:1075px;background:var(--mint)}
.services-panel{position:absolute;left:44px;top:1220px;width:1112px;height:745px;background:var(--dark)}
.card{position:absolute;top:1413px;width:250px;height:407px;background:var(--white);border-radius:3px}
.card .shot{position:absolute;left:0;top:0;width:250px;height:186px;border-radius:3px 3px 0 0}
.card .inner{position:absolute;left:10px;top:200px;width:230px;height:196px;background:var(--grey-box);border-radius:2px;text-align:center}
.card.active .inner{background:var(--green);color:var(--white)}
.card .icon{position:absolute;left:89px;top:158px;width:72px;height:72px;border-radius:50%;background:var(--white);border:3px solid #dfe9d9;display:flex;align-items:center;justify-content:center}
.card h3{margin-top:51px;font-size:13px;font-weight:600}
.card p{margin:13px auto 0;width:200px;font-size:9.4px;line-height:15.5px}
.card .more{position:absolute;left:65px;top:144px;width:100px;height:30px;border:1.5px solid var(--green);background:var(--white);color:var(--green);font-size:9.5px;font-weight:600;display:flex;align-items:center;justify-content:center}

/* areas */
.area-list{position:absolute;left:75px;top:2176px;width:411px;display:grid;grid-template-columns:211px 200px}
.area-list li{list-style:none;height:49px;border-top:1px solid #d9e3d3;display:flex;align-items:center;padding-left:20px;gap:12px;font-size:14px}
.area-list li.sel{background:#d7e6cf;color:var(--green);font-weight:600}
.map{position:absolute;left:531px;top:2176px;width:594px;height:469px;background:linear-gradient(135deg,#cfeadb 0%,#def2e2 40%,#cbe7d4 70%,#d9efe0 100%)}

/* testimonials */
.testimonials{position:absolute;left:0;top:2617px;width:1200px;height:593px;background:var(--dark)}
.testimonials .section-title{color:var(--green);top:103px}
.quote{position:absolute;left:437px;top:288px;width:470px;color:var(--white);font-size:15px;line-height:21px}
.arrow{position:absolute;top:432px;width:26px;height:26px;border:1px solid var(--green);border-radius:50%;display:flex;align-items:center;justify-content:center}

/* contact */
.feature{position:absolute;left:200px;display:flex;align-items:center;gap:30px;font-size:12px;font-weight:600}
.feature .ic{width:62px;height:62px;border-radius:50%;background:#e4eee0;display:flex;align-items:center;justify-content:center}
.quote-card{position:absolute;left:613px;top:3417px;width:386px;height:406px;border-radius:8px;background:linear-gradient(180deg,#eeeeee 0%,#e5eddf 55%,#d0ecc2 100%)}
.quote-card h2{margin-top:42px;text-align:center;font-size:20px;font-weight:600;line-height:23px}
.field{position:absolute;height:36px;background:var(--white);border-radius:20px;font-size:9px;padding:12px 0 0 19px;color:var(--text)}
.terms{position:absolute;left:0;width:386px;top:360px;text-align:center;font-size:9px}
.terms u{font-weight:600}

/* footer */
.site-footer{position:absolute;left:0;top:3917px;width:1200px;height:296px;background:linear-gradient(180deg,#3a4a33 0%,#2f3a2b 40%,#262c23 100%)}
.site-footer .col{position:absolute;top:64px;color:var(--white)}
.site-footer h4{font-size:13.5px;font-weight:500;margin-bottom:16px}
.site-footer .col p,.site-footer .col li{font-size:9px;line-height:20px;list-style:none}
.vline{position:absolute;top:30px;width:1px;height:160px;background:rgba(255,255,255,.25)}
.social{display:flex;gap:12px;margin-top:18px}
.social i{width:25px;height:25px;border-radius:50%;border:1px solid rgba(255,255,255,.7);display:block}
.footer-brand{position:absolute;left:200px;top:64px;display:flex;align-items:center;gap:8px;color:var(--white);font-size:17px;font-weight:700;line-height:20px}
.footer-brand .mark{width:12px;height:12px;background:var(--green)}
.copy{position:absolute;top:264px;font-size:9px;color:var(--white)}
</style>
</head>
<body>
<div class="page">

  <section class="hero" role="img" aria-label="Cleared earthen land beneath a forested hillside under a cloudy sky">
    <h1>Shaping Ground with<br>Care and Grit</h1>
    <a class="btn btn-white" style="left:200px;top:373px;width:125px;height:36px">Get a Free Quote</a>
    <a class="btn btn-green" style="left:338px;top:373px;width:123px;height:36px">View Services</a>
    <div class="dots"><i></i><i class="on"></i><i></i><i></i></div>
  </section>

  <header class="site-header">
    <nav class="nav">
      <a class="current">Home</a><a>About Us</a><a>Services</a><a>Testimonials</a><a>Service Area</a><a>Contact Us</a>
    </nav>
    <div class="header-phone">
      <svg width="11" height="11" viewBox="0 0 24 24"><path fill="none" stroke="#4a9a2c" stroke-width="2.2" d="M5 3h4l2 5-3 2a12 12 0 0 0 6 6l2-3 5 2v4a2 2 0 0 1-2 2A18 18 0 0 1 3 5a2 2 0 0 1 2-2z"/></svg>
      1 (555) 014-2290
    </div>
    <a class="btn btn-green" style="left:1000px;top:19px;width:125px;height:37px">Get a Free Quote</a>
  </header>
  <div class="brand-badge"><i class="mark"></i><span>Brack<br>and<br>Loam</span></div>

  <section class="about">
    <div class="about-frame"></div>
    <div class="rule" style="left:100px;top:813px;width:194px"></div>
    <h2 class="section-title">About Brack and Loam LLC</h2>
    <p class="sub">Lorem Ipsum is simply dummy text of the printing and typesetting industry.</p>
    <p class="body" style="top:895px">There are many variations of passages of Lorem Ipsum available, but the majority have suffered alteration in some form, by injected humour, or randomised words which don't look even slightly believable.</p>
    <p class="body" style="top:942px">If you are going to use a passage of Lorem Ipsum, you need to be sure there isn't anything embarrassing hidden in the middle of text. All the Lorem Ipsum generators on the Internet tend to repeat predefined chunks as necessary, making this the first true generator on the Internet.</p>
    <a class="btn btn-outline" style="left:200px;top:1016px;width:125px;height:36px">Discover More</a>
    <div class="photo-circle" style="left:768px;top:719px;width:357px;height:357px;background:linear-gradient(160deg,#9aa0a3 0%,#6b5a48 45%,#7a5a3e 70%,#8a6a4a 100%)" role="img" aria-label="Orange skid steer clearing trees in a wooded lot"></div>
    <div class="photo-circle" style="left:822px;top:976px;width:166px;height:166px;border:5px solid #fff;background:linear-gradient(180deg,#b9c7a0 0%,#7c8f63 45%,#8a8c8e 70%,#c9c3b4 100%)" role="img" aria-label="Grey dump truck parked beside greenery"></div>
  </section>

  <div class="services-band"></div>
  <section class="services-panel"></section>
  <h2 class="section-title" style="top:1280px;color:#fff">Exceptional Services We Offer</h2>
  <div class="rule" style="left:44px;top:1362px;width:300px;background:#777"></div>
  <p class="lead" style="top:1350px;color:#fff;width:610px">Lorem Ipsum is simply dummy text of the printing and typesetting industry. Standard &nbsp;the 1500s, when an unknown printer took a galley</p>

  <article class="card" style="left:200px">
    <div class="shot" role="img" aria-label="Excavator grading a cleared lot near a city skyline" style="background:linear-gradient(180deg,#9fc6e6 0%,#c7dbe8 45%,#b09a78 65%,#9c8464 100%)"></div>
    <div class="inner"><h3>Land Clearing &amp; Grading</h3><p>Lorem Ipsum is simply dummy text of the printing and typesetting industry standard dummy text ever since...</p><span class="more">Read More</span></div>
    <div class="icon"><svg width="40" height="40" viewBox="0 0 40 40" fill="none" stroke="#4a9a2c" stroke-width="1.6"><path d="M6 24c4-10 24-10 28 0"/><path d="M6 24h28M9 28h22M12 32h16"/><path d="M13 18l4-5 4 4 4-3 4 5"/></svg></div>
  </article>
  <article class="card" style="left:474px">
    <div class="shot" role="img" aria-label="Mulched forest track between tall conifers" style="background:linear-gradient(180deg,#7e8a84 0%,#3f5a3a 40%,#6b4f3c 70%,#8a6a52 100%)"></div>
    <div class="inner"><h3>Forestry Mulching</h3><p>Lorem Ipsum is simply dummy text of the printing and typesetting industry standard dummy text ever since...</p><span class="more">Read More</span></div>
    <div class="icon"><svg width="40" height="40" viewBox="0 0 40 40" fill="none" stroke="#4a9a2c" stroke-width="1.6"><circle cx="15" cy="15" r="6"/><circle cx="25" cy="13" r="6"/><path d="M15 21v10M25 19v12M6 31h28M8 35h24"/></svg></div>
  </article>
  <article class="card active" style="left:749px">
    <div class="shot" role="img" aria-label="Freshly repaired gravel driveway through a grassy field" style="background:linear-gradient(180deg,#c5d6e2 0%,#9fb38a 35%,#8a8a82 60%,#7d7d78 100%)"></div>
    <div class="inner"><h3>Gravel Driveway Repair</h3><p>Lorem Ipsum is simply dummy text of the printing and typesetting industry standard dummy text ever since...</p><span class="more">Read More</span></div>
    <div class="icon"><svg width="40" height="40" viewBox="0 0 40 40" fill="none" stroke="#4a9a2c" stroke-width="1.6"><path d="M14 6c-4 10 4 18-2 28M26 6c4 10-4 18 2 28M20 8v4M20 16v4M20 24v4"/></svg></div>
  </article>
  <a class="btn btn-green" style="left:531px;top:1855px;width:138px;height:36px">View All Services</a>

  <h2 class="section-title" style="top:2042px">Areas We Serve</h2>
  <div class="rule" style="left:0;top:2124px;width:344px"></div>
  <p class="lead" style="top:2112px">We're proud to serve <b>North Georgia, and the surrounding areas</b> with our quality services.</p>
  <ul class="area-list">
    <li><svg width="9" height="12" viewBox="0 0 10 14"><path fill="#4a9a2c" d="M5 0a5 5 0 0 1 5 5c0 4-5 9-5 9S0 9 0 5a5 5 0 0 1 5-5z"/><circle cx="5" cy="5" r="1.8" fill="#fff"/></svg>Stockbridge</li>
    <li><svg width="9" height="12" viewBox="0 0 10 14"><path fill="#4a9a2c" d="M5 0a5 5 0 0 1 5 5c0 4-5 9-5 9S0 9 0 5a5 5 0 0 1 5-5z"/><circle cx="5" cy="5" r="1.8" fill="#fff"/></svg>McDonough</li>
    <li class="sel"><svg width="9" height="12" viewBox="0 0 10 14"><path fill="#4a9a2c" d="M5 0a5 5 0 0 1 5 5c0 4-5 9-5 9S0 9 0 5a5 5 0 0 1 5-5z"/><circle cx="5" cy="5" r="1.8" fill="#fff"/></svg>Locust Grove</li>
    <li><svg width="9" height="12" viewBox="0 0 10 14"><path fill="#4a9a2c" d="M5 0a5 5 0 0 1 5 5c0 4-5 9-5 9S0 9 0 5a5 5 0 0 1 5-5z"/><circle cx="5" cy="5" r="1.8" fill="#fff"/></svg>Hampton</li>
    <li><svg width="9" height="12" viewBox="0 0 10 14"><path fill="#4a9a2c" d="M5 0a5 5 0 0 1 5 5c0 4-5 9-5 9S0 9 0 5a5 5 0 0 1 5-5z"/><circle cx="5" cy="5" r="1.8" fill="#fff"/></svg>Ellenwood</li>
    <li><svg width="9" height="12" viewBox="0 0 10 14"><path fill="#4a9a2c" d="M5 0a5 5 0 0 1 5 5c0 4-5 9-5 9S0 9 0 5a5 5 0 0 1 5-5z"/><circle cx="5" cy="5" r="1.8" fill="#fff"/></svg>Rex</li>
    <li><svg width="9" height="12" viewBox="0 0 10 14"><path fill="#4a9a2c" d="M5 0a5 5 0 0 1 5 5c0 4-5 9-5 9S0 9 0 5a5 5 0 0 1 5-5z"/><circle cx="5" cy="5" r="1.8" fill="#fff"/></svg>Conley</li>
    <li><svg width="9" height="12" viewBox="0 0 10 14"><path fill="#4a9a2c" d="M5 0a5 5 0 0 1 5 5c0 4-5 9-5 9S0 9 0 5a5 5 0 0 1 5-5z"/><circle cx="5" cy="5" r="1.8" fill="#fff"/></svg>Morrow</li>
    <li><svg width="9" height="12" viewBox="0 0 10 14"><path fill="#4a9a2c" d="M5 0a5 5 0 0 1 5 5c0 4-5 9-5 9S0 9 0 5a5 5 0 0 1 5-5z"/><circle cx="5" cy="5" r="1.8" fill="#fff"/></svg>Forest Park</li>
    <li><svg width="9" height="12" viewBox="0 0 10 14"><path fill="#4a9a2c" d="M5 0a5 5 0 0 1 5 5c0 4-5 9-5 9S0 9 0 5a5 5 0 0 1 5-5z"/><circle cx="5" cy="5" r="1.8" fill="#fff"/></svg>Lake City</li>
    <li><svg width="9" height="12" viewBox="0 0 10 14"><path fill="#4a9a2c" d="M5 0a5 5 0 0 1 5 5c0 4-5 9-5 9S0 9 0 5a5 5 0 0 1 5-5z"/><circle cx="5" cy="5" r="1.8" fill="#fff"/></svg>Conyers</li>
    <li><svg width="9" height="12" viewBox="0 0 10 14"><path fill="#4a9a2c" d="M5 0a5 5 0 0 1 5 5c0 4-5 9-5 9S0 9 0 5a5 5 0 0 1 5-5z"/><circle cx="5" cy="5" r="1.8" fill="#fff"/></svg>Jonesboro</li>
  </ul>
  <a class="btn btn-outline" style="left:75px;top:2506px;width:100px;height:34px;background:#fff">View All</a>
  <div class="map" role="img" aria-label="Embedded service area map with location pins"></div>

  <section class="testimonials">
    <h2 class="section-title">Happy Clients Say</h2>
    <div class="rule" style="top:185px;width:344px;background:#666"></div>
    <div class="photo-circle" style="left:200px;top:217px;width:181px;height:181px;background:linear-gradient(180deg,#a9c4de 0%,#6f8f5a 45%,#6a5644 75%,#5c4a3a 100%)" role="img" aria-label="Excavator working on a cleared hillside site"></div>
    <div class="abs" style="left:261px;top:388px;color:#f2c21b;font-size:10px;letter-spacing:1px">★★★★★</div>
    <div class="abs" style="left:231px;top:418px;color:#fff;font-size:13.5px;font-weight:500">Standard Chunk</div>
    <div class="abs" style="left:231px;top:438px;color:#ddd;font-size:10px">New York</div>
    <svg class="abs" style="left:437px;top:230px" width="30" height="22" viewBox="0 0 30 22"><path fill="#4a9a2c" d="M0 0h12v10L7 22H1l5-11H0zM17 0h12v10l-5 12h-6l5-11h-6z"/></svg>
    <div class="quote"><p>“ It is a long established fact that a reader will be distracted by the readable content of a page when looking at its layout.</p><p style="margin-top:20px">The point of using lorem Ipsum is that it has a more-or-less normal distribution readable English. ”</p></div>
    <div class="arrow" style="left:437px"><svg width="10" height="10" viewBox="0 0 10 10"><path d="M9 5H1M4 2L1 5l3 3" stroke="#fff" fill="none"/></svg></div>
    <div class="arrow" style="left:476px"><svg width="10" height="10" viewBox="0 0 10 10"><path d="M1 5h8M6 2l3 3-3 3" stroke="#fff" fill="none"/></svg></div>
    <a class="btn btn-outline-light" style="left:437px;top:481px;width:113px;height:36px">View All</a>
  </section>

  <h2 class="section-title" style="top:3286px">We handle everything for you!</h2>
  <div class="rule" style="top:3365px;width:344px"></div>
  <p class="lead" style="top:3355px;width:620px">Lorem Ipsum is simply dummy text of the printing and typesetting industry. Standard dummy text ever since the 1500s, when an unknown printer took a galley</p>

  <div class="feature" style="top:3443px"><span class="ic"><svg width="30" height="30" viewBox="0 0 24 24"><path fill="none" stroke="#555" stroke-width="1.3" d="M5 3h4l2 5-3 2a12 12 0 0 0 6 6l2-3 5 2v4a2 2 0 0 1-2 2A18 18 0 0 1 3 5a2 2 0 0 1 2-2zM15 3a6 6 0 0 1 6 6M15 6a3 3 0 0 1 3 3"/></svg></span>One Call Away</div>
  <div class="feature" style="top:3518px"><span class="ic"><svg width="28" height="28" viewBox="0 0 24 24" fill="none" stroke="#555" stroke-width="1.3"><rect x="5" y="4" width="14" height="17" rx="1"/><path d="M9 2h6v4H9zM8 10h8M8 13h8M8 16h5"/></svg></span>Get No Cost Estimate</div>
  <div class="feature" style="top:3593px"><span class="ic"><svg width="28" height="28" viewBox="0 0 24 24" fill="none" stroke="#555" stroke-width="1.3"><path d="M7 13v8h4l5-3v-5l-4-1-2-4-3 5zM4 13h3v8H4z"/><path d="M12 3l.7 1.5 1.6.2-1.2 1.1.3 1.6-1.4-.8-1.4.8.3-1.6-1.2-1.1 1.6-.2zM18 6l.5 1 1 .1-.8.7.2 1-.9-.5-.9.5.2-1-.8-.7 1-.1z"/></svg></span>Satisfaction Guaranteed</div>
  <div class="feature" style="top:3669px"><span class="ic"><svg width="28" height="28" viewBox="0 0 24 24" fill="none" stroke="#555" stroke-width="1.3"><path d="M5 14v-3a7 7 0 0 1 14 0v3"/><rect x="3" y="13" width="4" height="6" rx="1"/><rect x="17" y="13" width="4" height="6" rx="1"/><path d="M19 19c0 2-3 3-6 3"/></svg></span>Support After Services</div>
  <a class="btn btn-outline" style="left:200px;top:3763px;width:138px;height:36px">Contact Us Today!</a>

  <div class="quote-card">
    <h2>Get a Free<br>Personalized Quote</h2>
    <div class="field" style="left:24px;top:122px;width:163px">First name</div>
    <div class="field" style="left:199px;top:122px;width:163px">Last name</div>
    <div class="field" style="left:24px;top:172px;width:338px">Email...</div>
    <div class="field" style="left:24px;top:222px;width:163px">Phone</div>
    <div class="field" style="left:199px;top:222px;width:163px">ZIP code</div>
    <div class="field" style="left:24px;top:272px;width:338px;height:63px;border-radius:12px">Message...</div>
    <p class="terms">You also agree to our <u>Terms of Service.</u></p>
  </div>
  <a class="btn btn-dark" style="left:737px;top:3805px;width:138px;height:36px">Get a Quote</a>

  <footer class="site-footer" role="img" aria-label="Dark forest backdrop">
    <div class="rule" style="left:384px;top:30px;width:616px;background:rgba(255,255,255,.25)"></div>
    <div class="footer-brand"><i class="mark"></i><span>Brack and<br>Loam LLC</span></div>
    <div class="vline" style="left:384px"></div>
    <div class="col" style="left:406px">
      <h4>Contact Us</h4>
      <p>☏ &nbsp;1 (555) 014-2290</p>
      <p>✉ &nbsp;contact@brackandloam.com</p>
      <p style="line-height:16px;margin-top:4px;width:150px">⌖ &nbsp;212 E Sample Street, # Suite, QX 40917</p>
    </div>
    <div class="vline" style="left:613px"></div>
    <div class="col" style="left:638px">
      <h4>Quick Links</h4>
      <ul><li>Home</li><li>About Us</li><li>Services</li><li>Testimonials</li><li>Service Area</li><li>Contact Us</li></ul>
    </div>
    <div class="vline" style="left:795px"></div>
    <div class="col" style="left:818px">
      <h4>Opening Hours</h4>
      <p>Mon - Fri: <span style="margin-left:36px">08:00 AM - 6:00 PM</span></p>
      <p>Sat: <span style="margin-left:64px">10:00 AM - 2:00 PM</span></p>
      <p>Sun: <span style="margin-left:62px">Closed</span></p>
      <div class="social"><i></i><i></i><i></i><i></i></div>
    </div>
    <p class="copy" style="left:200px">© 2025 <span style="color:var(--green)">Brack and Loam LLC.</span> All Right Reserved</p>
    <p class="copy" style="left:638px">Terms and conditions &nbsp;&nbsp; | &nbsp;&nbsp; Privacy policy</p>
    <svg class="abs" style="left:1118px;top:234px" width="12" height="14" viewBox="0 0 12 14"><path d="M6 1l5 12H1z" fill="#4a9a2c"/></svg>
  </footer>

</div>
</body>
</html>
```